Renate Falkner
Heilpraktikerin eingeschränkt auf den Bereich der Psychotherapie
Ausbildungen:
Diplom Sozialpädagogin (FH)
Systemische Sucht- Paar- und Familientherapeutin
Schwerpunkte:
-Beratungen in Lebenskrisen
-Burn Out
-Suchttherapie
-Einzeltherapie
- Gruppentherapie
-Paartherapie
- Familientherapie
Arbeiten mit:
-Familienrekonstruktion
-Symbolen
-Skulpturen
-Empathie
-Verständnis
...Wir sollten heiter Raum um Raum durchschreiten und an keinem wie an einer Heimat hängen. Der Weltgeist will nicht fesseln und uns engen, er will uns Stuf um Stufe heben, weiten...
Wohlan denn Herz nimm Abschied und gesunde
(Gustav Lindner: "Wellen")

```html
<!DOCTYPE html>
<html lang="de">
<head>
<meta charset="utf-8">
<title>Renate Falkner – Flyer</title>
<link rel="stylesheet" href="https://fonts.googleapis.com/css2?family=Pinyon+Script&family=Tinos:ital,wght@0,400;1,400&family=Source+Sans+3:ital,wght@0,400;1,400&display=swap">
<style>
  :root {
    --green: #8dc025;
    --green-deep: #6c9f16;
    --green-pale: #dcebb8;
    --purple: #7d1f70;
    --ink: #2b2b2b;
    --grey: #555;
    --white: #ffffff;
    --stage: #ebe8e3;
  }
  * { margin: 0; padding: 0; box-sizing: border-box; }
  html, body { width: 1200px; height: 750px; overflow: hidden; }
  body { background: var(--stage); position: relative; }

  .flyer {
    position: absolute;
    top: 65px;
    width: 438px;
    height: 620px;
    background: var(--white);
    box-shadow: 0 6px 18px rgba(0,0,0,.18);
    overflow: hidden;
  }
  .flyer--front { left: 122px; }
  .flyer--back { left: 640px; }
  .flyer__art { position: absolute; inset: 0; width: 100%; height: 100%; }

  /* front */
  .brand-name {
    position: absolute; left: 40px; top: 52px;
    font-family: "Pinyon Script", cursive;
    font-size: 46px; color: var(--purple); line-height: 1;
  }
  .profession {
    position: absolute; left: 48px; top: 132px;
    font-family: "Tinos", serif;
  }
  .profession__title { font-size: 13px; color: var(--purple); letter-spacing: .02em; }
  .profession__scope { font-size: 11.5px; color: var(--grey); margin-top: 3px; }

  .quote {
    position: absolute; left: 36px; right: 30px; top: 446px;
    font-family: "Source Sans 3", sans-serif;
    color: var(--white); font-size: 13.5px; line-height: 1.42;
  }
  .quote__initial {
    font-family: "Tinos", serif; color: var(--purple);
    font-size: 40px; float: left; line-height: .8; margin: 2px 3px 0 0;
  }
  .quote__source {
    display: block; text-align: right; margin-top: 22px;
    font-style: italic; font-size: 12px; color: rgba(255,255,255,.92);
  }

  /* back */
  .profile {
    position: absolute; left: 34px; top: 68px; width: 225px;
    font-family: "Tinos", serif; font-size: 12.5px; line-height: 17px; color: var(--ink);
  }
  .profile__heading { color: var(--purple); font-size: 12.5px; letter-spacing: .02em; }
  .profile__section + .profile__section { margin-top: 12px; }
  .profile__list { list-style: none; }
  .profile__list li { position: relative; padding-left: 10px; }
  .profile__list li::before {
    content: ""; position: absolute; left: 0; top: 7px;
    width: 4px; height: 4px; border-radius: 50%; background: var(--purple);
  }

  .contact {
    position: absolute; left: 34px; top: 500px;
    font-family: "Source Sans 3", sans-serif; font-size: 11.5px; line-height: 17px; color: var(--ink);
  }
  .contact__note { font-style: italic; margin-top: 6px; }
</style>
</head>
<body>

<section class="flyer flyer--front">
  <svg class="flyer__art" viewBox="0 0 438 620" aria-hidden="false">
    <defs>
      <linearGradient id="frontPhoto" x1="0" y1="0" x2="1" y2="1">
        <stop offset="0" stop-color="#ffffff"/>
        <stop offset=".45" stop-color="#eef5de"/>
        <stop offset=".7" stop-color="#b7d77a"/>
        <stop offset="1" stop-color="#e9f2d8"/>
      </linearGradient>
    </defs>
    <path role="img" aria-label="Foto: grüner Grashalm mit Wassertropfen"
          d="M0 0 H438 V250 C330 300 170 330 0 350 Z" fill="url(#frontPhoto)"/>
    <path d="M0 372 C150 352 300 318 438 268 V620 H0 Z" fill="var(--green)"/>
    <path d="M0 372 C150 352 300 318 438 268 V292 C300 338 150 370 0 392 Z" fill="var(--green-deep)" opacity=".25"/>
  </svg>

  <h1 class="brand-name">Renate Falkner</h1>
  <div class="profession">
    <p class="profession__title">HEILPRAKTIKERIN</p>
    <p class="profession__scope">eingeschränkt auf den Bereich der Psychotherapie</p>
  </div>

  <blockquote class="quote">
    <span class="quote__initial">W</span>ir sollten heiter Raum um Raum durchschreiten
    und an keinem wie an einer Heimat hängen.
    Der Weltgeist will nicht fesseln und uns engen,
    er will uns Stuf um Stufe heben, weiten...
    Wohlan denn Herz nimm Abschied und gesunde
    <cite class="quote__source">(Gustav Lindner: „Wellen“)</cite>
  </blockquote>
</section>

<section class="flyer flyer--back">
  <svg class="flyer__art" viewBox="0 0 438 620">
    <defs>
      <linearGradient id="backPhoto" x1="0" y1="0" x2="1" y2="1">
        <stop offset="0" stop-color="#eef5de"/>
        <stop offset=".4" stop-color="#a9cf62"/>
        <stop offset=".75" stop-color="#f4f8ec"/>
        <stop offset="1" stop-color="#dcebb8"/>
      </linearGradient>
      <linearGradient id="backFaint" x1="0" y1="0" x2="0" y2="1">
        <stop offset="0" stop-color="#eef4e2"/>
        <stop offset=".5" stop-color="#ffffff"/>
      </linearGradient>
    </defs>
    <rect x="0" y="0" width="262" height="450" fill="url(#backFaint)"/>
    <rect role="img" aria-label="Foto: Grashalm mit Wassertropfen, Ausschnitt"
          x="268" y="0" width="170" height="420" fill="url(#backPhoto)"/>
    <rect x="262" y="0" width="6" height="440" fill="var(--green)"/>
    <path d="M0 458 C150 452 320 430 438 396 V620 H0 Z" fill="var(--green)"/>
  </svg>

  <div class="profile">
    <div class="profile__section">
      <h2 class="profile__heading">AUSBILDUNGEN:</h2>
      <p>Diplom Sozialpädagogin (FH)<br>Systemische Sucht- Paar- und Familientherapeutin</p>
    </div>
    <div class="profile__section">
      <h2 class="profile__heading">SCHWERPUNKTE:</h2>
      <ul class="profile__list">
        <li>Beratungen in Lebenskrisen</li>
        <li>Burn Out</li>
        <li>Suchttherapie</li>
        <li>Einzeltherapie</li>
        <li>Gruppentherapie</li>
        <li>Paartherapie</li>
        <li>Familientherapie</li>
      </ul>
    </div>
    <div class="profile__section">
      <h2 class="profile__heading">ARBEITEN MIT:</h2>
      <ul class="profile__list">
        <li>Familienrekonstruktion</li>
        <li>Symbolen</li>
        <li>Skulpturen</li>
        <li>Empathie</li>
        <li>Verständnis</li>
      </ul>
    </div>
  </div>

  <address class="contact" style="font-style:normal">
    <p>Renate Falkner • Lindenweg 12 • 82340 Feldkirchen</p>
    <p>Tel.: 08152/444 20 80 • mobil: 0171/ 4825903</p>
    <p>e-Mail: renate.falkner@mailpost.de</p>
    <p class="contact__note">Termine nach Vereinbarung</p>
  </address>
</section>

</body>
</html>
```